Stationary for New Company

We need stationary designed for a new company. Details of the required stationary is attached.

The final version should be trendy, clean... only 2 colours (green + grey/black) and professional.

#1: Business Cards (design on 2 sides)
#2: Letterhead (word format)
#3: Cover Page and back cover for proposals
#4: Envelopes,
#5: Thank You card,
#6: Presentation Folder,
#7: Email signatures template (sample attached in word document)

Logo is attached. Logo can be reversed out (will attach once available). Logo can be stacked or horizontal (provided as horizontal).

Files need to be provided in ai + png format.

Target Market(s)

Business owners. More affluent.

Industry/Entity Type

Business

Requirements
Must have
• See brief

Font: Calibri
Should not have
• Photographs / stock photos

```html
<!DOCTYPE html>
<html lang="en">
<head>
<meta charset="utf-8">
<title>Larkfield Insurance Brokers – Business Cards</title>
<link rel="stylesheet" href="https://fonts.googleapis.com/css2?family=Open+Sans:ital,wght@0,300;0,400;0,600;1,400&display=swap">
<style>
  :root {
    --backdrop: #cfcfcf;
    --card-dark: #2b2a2b;
    --card-light: #f7f7f5;
    --brand-green: #5f9631;
    --text-light: #d6d6d6;
    --text-muted: #9a9a9a;
  }
  * { margin: 0; padding: 0; box-sizing: border-box; }
  html, body { width: 1200px; height: 1000px; overflow: hidden; }
  body {
    background: var(--backdrop);
    font-family: "Open Sans", sans-serif;
    position: relative;
  }
  .card {
    position: absolute;
    width: 490px;
    height: 280px;
    border-radius: 2px;
    overflow: hidden;
    box-shadow: 0 3px 8px rgba(0,0,0,0.18);
  }
  .card-front {
    left: 130px;
    top: 170px;
    background: var(--card-dark);
    display: flex;
    align-items: center;
    justify-content: center;
  }
  .card-back {
    left: 580px;
    top: 540px;
    background: var(--card-light);
  }
  .brand {
    display: flex;
    align-items: center;
    gap: 10px;
  }
  .brand-square {
    width: 38px;
    height: 38px;
    background: var(--brand-green);
  }
  .brand-name {
    font-weight: 400;
    color: var(--brand-green);
    line-height: 1.1;
  }
  .card-front .brand-name { font-size: 26px; }
  .card-back .brand {
    position: absolute;
    right: 26px;
    top: 28px;
    gap: 8px;
  }
  .card-back .brand-square { width: 28px; height: 28px; }
  .card-back .brand-name { font-size: 18px; }
  .brand-sub {
    display: block;
    font-size: 0.5em;
  }
  .wave {
    position: absolute;
    inset: 0;
    width: 100%;
    height: 100%;
  }
  .wave path { fill: var(--card-dark); }
  .contact {
    position: absolute;
    left: 26px;
    bottom: 20px;
    width: 440px;
  }
  .contact-rule {
    width: 300px;
    height: 1px;
    background: var(--brand-green);
    margin-bottom: 10px;
  }
  .person-name {
    font-size: 16px;
    font-weight: 300;
    color: var(--text-light);
    line-height: 1.3;
  }
  .person-title {
    font-size: 13px;
    font-style: italic;
    color: var(--brand-green);
    line-height: 1.3;
    margin-bottom: 5px;
  }
  .contact-line {
    font-size: 8px;
    color: var(--text-muted);
    line-height: 1.55;
  }
  .contact-label { color: var(--brand-green); }
  .sep { margin: 0 5px; color: var(--text-muted); }
</style>
</head>
<body>
  <section class="card card-front" aria-label="Business card front">
    <div class="brand">
      <span class="brand-square"></span>
      <span class="brand-name">Larkfield<span class="brand-sub">Insurance Brokers</span></span>
    </div>
  </section>

  <section class="card card-back" aria-label="Business card back">
    <svg class="wave" viewBox="0 0 490 280" preserveAspectRatio="none" aria-hidden="true">
      <path d="M0,68 C45,72 95,130 185,130 C285,130 385,100 490,95 L490,280 L0,280 Z"/>
    </svg>
    <div class="brand">
      <span class="brand-square"></span>
      <span class="brand-name">Larkfield<span class="brand-sub">Insurance Brokers</span></span>
    </div>
    <div class="contact">
      <div class="contact-rule"></div>
      <p class="person-name">Daniel Reeve, BA, CRM</p>
      <p class="person-title">President &amp; CEO</p>
      <p class="contact-line"><span class="contact-label">Address:</span> 2210 Maple Ridge Road NW Calgary, AB T3A 1K7</p>
      <p class="contact-line"><span class="contact-label">Phone:</span> 403.555.0140<span class="sep">|</span><span class="contact-label">Direct:</span> 403.555.0177</p>
      <p class="contact-line"><span class="contact-label">Fax:</span> 403.555.0162<span class="sep">|</span><span class="contact-label">Toll Free:</span> 888.555.0193</p>
      <p class="contact-line"><span class="contact-label">Web:</span> dreeve@larkfieldinsurance.com<span class="sep">|</span>www.larkfieldinsurance.com</p>
    </div>
  </section>
</body>
</html>
```